Flyer o infografía informativa de un servicio óptico

Requerimos un machote que podamos estar editando según el cliente ( Nombre, logo e información ) estas son las consideraciones a seguir

-El público target son personas que laboran dentro de una compañía en todas las jerarquías y quieren mejorar su salud visual.
-Aceptamos propuestas de flyer o infografía altamente llamativa, con colores y/o imágenes que representen lo que estamos ofreciendo
-Debe tener el logo de TELVO Y PINAX ya sea en su formato blanco o negro, dichos logos se anexan en este concurso.
-Habrán 4 puntos que son la médula espinal del flyer/infografía
*Descuentos vía nómina
*3, 6, 9 y 12 meses sin intereses con todas las tarjetas de crédito.
*10% de descuento si pagas de contado
*Extensivo a familiares
-Existirán 5 puntos adicionales que se deberán incluir sin embargo no deberán tener la misma o más relevancia que los 4 puntos anteriores.
*Cirugías láser
*Convenio con aseguradoras
*50% descuento en examen pre-operatorio
*2 consultas post-operatorias sin costo
-Un texto informativo que tendrá esta estructura, "A todo el personal de <empresa> se les informa que nos presentaremos en sus instalaciones el <fecha> a las <hora> tendremos grandes promociones para su vista"

Toda la información detallada no se colocará per se, nos acercamos a ustedes para escuchar propuestas sin tanto texto, la finalidad de los puntos descritos es para que conozcan la oferta y puedan desarrollar sus propuestas.

Al final, el trabajo se debe entregar en formato de Adobe Illustrator para que pueda ser editado posteriormente.

```html
<!DOCTYPE html>
<html lang="es">
<head>
<meta charset="utf-8">
<title>Mejora tu visión – Flyer</title>
<link rel="stylesheet" href="https://fonts.googleapis.com/css2?family=Arimo:wght@400;700&display=swap">
<style>
  :root {
    --stage: #d9d9d9;
    --paper: #ffffff;
    --navy: #1b2a8c;
    --blue: #1f6fb8;
    --blue-light: #4aa3e0;
    --blue-dark: #16507f;
    --banner: #c9cdd3;
    --ink: #1a1a1a;
    --soft: #eef0f3;
    --photo-a: #e9d7cf;
    --photo-b: #b8a39c;
    --photo-c: #f4f4f4;
  }
  * { box-sizing: border-box; margin: 0; padding: 0; }
  html, body { width: 1200px; height: 1200px; overflow: hidden; background: var(--stage); font-family: "Arimo", Arial, sans-serif; }
  .flyer {
    position: absolute; left: 225px; top: 60px; width: 750px; height: 1080px;
    background: var(--paper); box-shadow: 0 6px 18px rgba(0,0,0,.25); overflow: hidden;
  }
  .hero-photo {
    position: absolute; left: 0; top: 0; width: 750px; height: 370px;
    background: linear-gradient(90deg, var(--photo-b) 0%, var(--photo-a) 45%, var(--photo-c) 75%, var(--photo-c) 100%);
  }
  .brand {
    position: absolute; left: 0; top: 19px; width: 338px; height: 131px;
    background: linear-gradient(135deg, var(--blue-dark), var(--blue-light));
    border-radius: 0 24px 24px 0; color: #fff; text-align: center; padding-top: 26px;
  }
  .brand-name { font-size: 38px; font-weight: 700; letter-spacing: 1px; }
  .brand-tagline { font-size: 13px; margin-top: 18px; opacity: .9; }
  .title-banner {
    position: absolute; left: 27px; top: 363px; width: 697px; height: 96px;
    background: var(--banner); border-radius: 24px;
    display: flex; align-items: center; justify-content: center;
    color: var(--navy); font-weight: 700; font-size: 74px; letter-spacing: -1px;
  }
  .extras {
    position: absolute; left: 25px; top: 513px; width: 341px; height: 314px;
    background: linear-gradient(135deg, var(--blue-light), var(--blue-dark));
    border-radius: 22px; color: #fff; padding: 22px 20px; list-style: none;
    font-size: 21px; font-weight: 700; line-height: 1.2;
  }
  .extras li { margin-bottom: 22px; }
  .benefit {
    position: absolute; left: 410px; width: 330px;
    display: flex; align-items: center; justify-content: center; text-align: center;
    font-weight: 700; font-size: 22px; line-height: 1.15; padding: 8px 16px 8px 80px;
    border-radius: 10px;
  }
  .benefit.is-blue { background: linear-gradient(135deg, var(--blue-light), var(--blue)); color: #fff; }
  .benefit.is-plain { background: var(--soft); color: var(--ink); border: 2px solid #d0d4da; }
  .benefit svg { position: absolute; left: 8px; top: 50%; transform: translateY(-50%); }
  .b1 { top: 491px; height: 104px; }
  .b2 { top: 591px; height: 78px; }
  .b3 { top: 677px; height: 79px; }
  .b4 { top: 773px; height: 65px; }
  .schedule-label { position: absolute; top: 900px; font-weight: 700; font-size: 30px; color: var(--ink); }
  .label-day { left: 33px; }
  .label-time { left: 341px; }
  .footer-band {
    position: absolute; left: 0; top: 997px; width: 750px; height: 83px;
    background: linear-gradient(180deg, #ffffff, #b9bcc2);
  }
</style>
</head>
<body>
  <main class="flyer">
    <div class="hero-photo" role="img" aria-label="Fotografía en primer plano de un ojo junto a una cartilla de agudeza visual"></div>
    <div class="brand">
      <div class="brand-name">TELVO y PINAX</div>
      <div class="brand-tagline">Salud visual para tu equipo</div>
    </div>
    <h1 class="title-banner">« Mejora tu visión »</h1>
    <ul class="extras">
      <li>* Cirugía láser</li>
      <li>* Convenio con aseguradoras</li>
      <li>* 50% de descuento en examen pre-operatorio</li>
      <li>* 2 consultas post-operatorias sin costo</li>
    </ul>

    <div class="benefit is-blue b1">
      <svg width="60" height="52" viewBox="0 0 60 52"><rect x="2" y="2" width="56" height="48" rx="8" fill="#16507f" stroke="#fff" stroke-width="3"/><path d="M17 27l9 9 17-19" fill="none" stroke="#fff" stroke-width="6" stroke-linecap="round" stroke-linejoin="round"/></svg>
      3, 6, 9 y 12 meses sin intereses en pagos con tarjeta de crédito
    </div>
    <div class="benefit is-plain b2">
      <svg width="60" height="52" viewBox="0 0 60 52"><rect x="2" y="2" width="56" height="48" rx="8" fill="#16507f" stroke="#fff" stroke-width="3"/><path d="M17 27l9 9 17-19" fill="none" stroke="#fff" stroke-width="6" stroke-linecap="round" stroke-linejoin="round"/></svg>
      10% de descuento en pago de contado
    </div>
    <div class="benefit is-blue b3">
      <svg width="60" height="52" viewBox="0 0 60 52"><rect x="2" y="2" width="56" height="48" rx="8" fill="#16507f" stroke="#fff" stroke-width="3"/><path d="M17 27l9 9 17-19" fill="none" stroke="#fff" stroke-width="6" stroke-linecap="round" stroke-linejoin="round"/></svg>
      Descuentos vía nómina
    </div>
    <div class="benefit is-plain b4">
      <svg width="60" height="52" viewBox="0 0 60 52"><rect x="2" y="2" width="56" height="48" rx="8" fill="#16507f" stroke="#fff" stroke-width="3"/><path d="M17 27l9 9 17-19" fill="none" stroke="#fff" stroke-width="6" stroke-linecap="round" stroke-linejoin="round"/></svg>
      Extensivo a familiares
    </div>

    <div class="schedule-label label-day">DÍA:</div>
    <div class="schedule-label label-time">HORARIO:</div>
    <div class="footer-band"></div>
  </main>
</body>
</html>
```